Brochure Design Project

I need a presentation folder with two inside pages and a pocket on back cover, use use my logo ,
make the cover just using the logo (put it big and centered, then use the logo in the background to fill, read the brief and make it modern, stop trying to make it exactly like the picture I gave as sample please use your talent trust your self
I just uploaded text for presentation folder
Target Market(s)
Dr's offices and patients

```html
<!DOCTYPE html>
<html lang="en">
<head>
<meta charset="utf-8">
<title>Steadfast Counseling – Presentation Folder</title>
<link rel="stylesheet" href="https://fonts.googleapis.com/css2?family=Roboto+Condensed:wght@400;700&family=Arimo:wght@400&display=swap">
<style>
  :root{
    --bg:#d9d9d9;
    --paper-light:#dcc07a;
    --paper-mid:#cfae60;
    --paper-dark:#b8974c;
    --pocket:#c7a557;
    --pocket-edge:#a98a40;
    --ink:#3b2b14;
    --brand:#6b3f1e;
    --disc:#8f8f8f;
    --disc-light:#b9b9b9;
    --card:#ffffff;
    --pocket-text:#f3e6c4;
    --label:#111111;
    --leader:#555555;
  }
  *{box-sizing:border-box;margin:0;padding:0}
  html,body{width:1200px;height:1000px;overflow:hidden}
  body{background:var(--bg);font-family:"Roboto Condensed",Arial,sans-serif;color:var(--ink);position:relative}

  .paper{position:absolute;overflow:hidden;background:linear-gradient(135deg,var(--paper-light) 0%,var(--paper-mid) 55%,var(--paper-dark) 100%);box-shadow:0 6px 16px rgba(0,0,0,.18)}

  /* wordmark: one colour, one weight */
  .wordmark{position:absolute;left:0;right:0;display:flex;align-items:center;justify-content:center;gap:10px;color:var(--brand);font-weight:700;font-size:28px;line-height:1.05}
  .wordmark__dot{flex:none;width:18px;height:18px;border-radius:50%;background:var(--brand)}

  /* front cover */
  .front-cover{left:60px;top:110px;width:240px;height:380px}
  .front-cover .wordmark{top:160px}

  /* inside spread */
  .inside-page{top:110px;width:230px;height:380px;padding:40px 16px 0}
  .inside-page--left{left:400px}
  .inside-page--right{left:630px}
  .body-copy{position:relative;font-size:6.6px;line-height:1.28;text-transform:uppercase;letter-spacing:.1px}
  .inside-page--left .body-copy{text-align:center}
  .body-copy p{margin-bottom:6px}
  .body-copy .closing{text-align:center}

  .disc{position:absolute;left:44px;top:226px}
  .pocket{position:absolute;left:0;bottom:0;width:100%;height:100px;background:var(--pocket);border-top:2px solid var(--pocket-edge);box-shadow:0 -2px 4px rgba(0,0,0,.12)}
  .pocket__title{position:absolute;left:0;right:0;top:50px;text-align:center;color:var(--pocket-text);font-weight:700;font-size:11px;letter-spacing:1px}
  .business-card{position:absolute;left:50px;top:14px;width:64px;height:42px;background:var(--card);border-radius:2px;box-shadow:0 1px 3px rgba(0,0,0,.25);color:var(--brand);font-weight:700;font-size:7px;display:flex;align-items:center;justify-content:center;gap:3px}
  .business-card .wordmark__dot{width:5px;height:5px}

  .callout{position:absolute;font-family:"Arimo",Arial,sans-serif;font-size:17px;letter-spacing:.5px;color:var(--label)}
  .callout--card{left:806px;top:432px}
  .callout--cd{left:354px;top:537px}
  .leader{position:absolute;left:0;top:0}

  /* outside spread */
  .outside-page{top:610px;width:260px;height:330px}
  .outside-page--back{left:650px}
  .outside-page--front{left:910px}
  .outside-page--front .wordmark{top:110px}
  .imprint{position:absolute;left:0;right:0;bottom:40px;text-align:center;font-size:6.5px;line-height:1.35;text-transform:uppercase}
</style>
</head>
<body>

<section class="paper front-cover" aria-label="Folder front cover">
  <div class="wordmark"><span class="wordmark__dot"></span><span>Steadfast<br>Counseling</span></div>
</section>

<section class="paper inside-page inside-page--left" aria-label="Inside left page">
  <div class="body-copy">
    <p>Steadfast Counseling is a proactive addiction counseling agency dedicated to address health issues in an integrated manner by working with pain management physicians to offer opioid education to prevent substance use and misuse disorders to their patients. Steadfast Counseling is a resource for pain management clinics to educate and provide prevention and counseling programs to patients to reduce the risk of substance use disorders for those patients at risk to pain related substance use disorders.</p>
    <p>Steadfast Counseling will provide education and prevention to individuals who are prescribed medications for health related reasons to prevent possible substance use disorders. Steadfast Counseling will receive referrals from pain management clinics to address this growing issue in healthcare.</p>
    <p>Counseling services are provided by addiction professionals who are experienced in working in all areas of addiction education and prevention and care.</p>
  </div>
  <svg class="disc" width="110" height="110" viewBox="0 0 110 110" aria-hidden="true">
    <circle cx="55" cy="55" r="52" fill="var(--disc)"/>
    <circle cx="55" cy="55" r="16" fill="var(--disc-light)"/>
    <circle cx="55" cy="55" r="6" fill="var(--pocket)"/>
    <text x="55" y="26" text-anchor="middle" font-family="Roboto Condensed, sans-serif" font-weight="700" font-size="8" fill="#ffffff">Steadfast</text>
  </svg>
  <div class="pocket">
    <div class="pocket__title">STEADFAST COUNSELING</div>
  </div>
</section>

<section class="paper inside-page inside-page--right" aria-label="Inside right page">
  <div class="body-copy">
    <p>Services offered<br>Pro active opioid education<br>Education materials to inform patients about the risk of taking medications inappropriately<br>Prevention services to educate patients about the risk and warning symptoms of substance misuse and abuse<br>Screening for potential substance use disorders related to prescribed medications<br>Assessment for substance use disorders related to medical issues and prescribed medications<br>Counseling provided by experienced addiction professionals to address substance related misuse and abuse for patients taking prescribed medications.</p>
    <p>Opioid education<br>Using opioids safely<br>The role of medications<br>Opioid agreements and contracts<br>Responsible use<br>Storing medication<br>Alcohol &amp; marijuana and pain medication<br>Over the counter medication<br>Storing your medication safely</p>
    <p class="closing">According to the Harlow Pain Institute more than 76 million Americans live with chronic pain. Pro active addiction counseling is needed!</p>
  </div>
  <div class="pocket">
    <div class="business-card"><span class="wordmark__dot"></span>Steadfast</div>
  </div>
</section>

<svg class="leader" width="1200" height="1000" aria-hidden="true">
  <polyline points="758,428 800,428" fill="none" stroke="var(--leader)" stroke-width="3"/>
  <polyline points="470,425 405,425 405,525" fill="none" stroke="var(--leader)" stroke-width="3"/>
</svg>
<div class="callout callout--card">YOUR BUSINESS CARD</div>
<div class="callout callout--cd">YOUR COMPANY CD</div>

<section class="paper outside-page outside-page--back" aria-label="Folder back cover">
  <div class="imprint">
    Steadfast Counseling Ltd<br>Your company address<br>Telephone<br>Fax<br>Your mail<br>Web
  </div>
</section>

<section class="paper outside-page outside-page--front" aria-label="Folder front cover, outside spread">
  <div class="wordmark"><span class="wordmark__dot"></span><span>Steadfast<br>Counseling</span></div>
</section>

</body>
</html>
```